Supplement Company Needs a Label Design

We need a label design for our pre-workout tub. Our company name is Quarry Athletics, we would like to emphasize the product's clinically dosed, science-based, transparent formula. We would like the label to mention our slogan "Iron Sharpens Iron." We would like you to experiment with colors and color schemes; the photo included is colorful, but that's not necessarily what we are looking for. We would like our main font & color scheme to match our theme of grittiness and boldness. We would like you to include how it boosts energy, enhances focus, creates bigger pumps, and elongates endurance. (Preferably on the back written vertically aside the supplement facts.) Photo 1 (Plume) is the guideline for the overall idea of what the pre-workout should look like, excluding color scheme and font. Photo 2(Redline Nutrition) is how we'd like to present the energy, focus, pumps, & endurance. This label shows the ingredients next to the supplement facts, however we'd like to show the boosted energy, enhanced focus, bigger pumps, and elongated endurance. The final design should communicate boldness, grit, but we would like it to remain uncluttered and clean looking.

Target Market(s)

Our target market is primarily males who workout in the gym.

Font styles to use
Other font styles liked:
• Blanka

Requirements
Nice to have
• Can incorporate the logo attached if you would like.

```html
<!DOCTYPE html>
<html lang="en">
<head>
<meta charset="utf-8">
<title>Quarry Pre Workout Label</title>
<link href="https://fonts.googleapis.com/css2?family=Montserrat:wght@300;400;600&display=swap" rel="stylesheet">
<style>
  :root {
    --page: #ffffff;
    --navy: #1b1f3b;
    --navy-deep: #161a33;
    --streak-red: #ff2a55;
    --streak-blue: #3b3f8f;
    --slogan-red: #d8193c;
    --ink-white: #ffffff;
    --edge: #c0204a;
  }
  * { margin: 0; padding: 0; box-sizing: border-box; }
  html, body {
    width: 1200px;
    height: 1200px;
    overflow: hidden;
    background: var(--page);
  }
  .canvas {
    position: relative;
    width: 1200px;
    height: 1200px;
  }
  .label {
    position: absolute;
    left: 196px;
    top: 456px;
    width: 808px;
    height: 288px;
    background: var(--navy);
    border: 1px solid var(--edge);
    overflow: hidden;
    font-family: "Montserrat", Arial, sans-serif;
    color: var(--ink-white);
  }
  .streaks {
    position: absolute;
    left: 150px;
    top: 0;
    width: 520px;
    height: 288px;
    background:
      linear-gradient(135deg,
        rgba(27,31,59,0) 18%,
        rgba(255,42,85,0.35) 34%,
        rgba(59,63,143,0.45) 46%,
        rgba(255,42,85,0.4) 60%,
        rgba(59,63,143,0.3) 72%,
        rgba(27,31,59,0) 88%);
    -webkit-mask-image: radial-gradient(ellipse at 55% 50%, #000 35%, transparent 75%);
    mask-image: radial-gradient(ellipse at 55% 50%, #000 35%, transparent 75%);
  }
  .brand-name {
    position: absolute;
    left: 0;
    width: 100%;
    top: 12px;
    text-align: center;
    font-weight: 600;
    font-size: 36px;
    letter-spacing: 4px;
    line-height: 40px;
  }
  .product-title {
    position: absolute;
    left: 304px;
    top: 98px;
    font-weight: 600;
    line-height: 1;
  }
  .product-title .line-pre { display: block; font-size: 42px; letter-spacing: 0.5px; }
  .product-title .line-workout { display: block; font-size: 46px; margin-top: -6px; letter-spacing: -0.5px; }
  .slogan {
    position: absolute;
    left: 310px;
    top: 169px;
    font-weight: 300;
    font-size: 19px;
    color: var(--slogan-red);
    white-space: nowrap;
  }
  .benefits {
    position: absolute;
    left: 499px;
    top: 100px;
    width: 80px;
    list-style: none;
    text-align: center;
  }
  .benefit {
    height: 47px;
    font-size: 8.5px;
    line-height: 9.5px;
  }
  .benefit svg { display: block; margin: 0 auto 3px; }
</style>
</head>
<body>
<div class="canvas">
  <section class="label">
    <div class="streaks" role="img" aria-label="Diagonal red and blue light streaks"></div>
    <div class="brand-name">QUARRY</div>
    <h1 class="product-title"><span class="line-pre">PRE</span><span class="line-workout">Workout</span></h1>
    <p class="slogan">Iron Sharpens Iron</p>
    <ul class="benefits">
      <li class="benefit">
        <svg width="14" height="16" viewBox="0 0 14 16"><path d="M8 0 L3 9 H7 L5 16 L11 6 H7 Z" fill="#fff"/></svg>
        Boosts<br>Energy
      </li>
      <li class="benefit">
        <svg width="16" height="16" viewBox="0 0 16 16"><circle cx="8" cy="8" r="6.5" fill="none" stroke="#fff" stroke-width="1.5"/><circle cx="8" cy="8" r="3.5" fill="none" stroke="#fff" stroke-width="1.5"/><circle cx="8" cy="8" r="1.2" fill="#fff"/></svg>
        Enhances<br>Focus
      </li>
      <li class="benefit">
        <svg width="16" height="16" viewBox="0 0 16 16"><path d="M8 2 L14 9 H10 V14 H6 V9 H2 Z" fill="#fff"/></svg>
        Creates Bigger<br>Pumps
      </li>
      <li class="benefit">
        <svg width="16" height="16" viewBox="0 0 16 16"><circle cx="8" cy="8" r="6.5" fill="none" stroke="#fff" stroke-width="1.5"/><path d="M8 4 V8 L11 10" fill="none" stroke="#fff" stroke-width="1.5"/></svg>
        Elongates<br>Endurance
      </li>
    </ul>
  </section>
</div>
</body>
</html>
```